Stationary design for boutique production house

We need a stationary design for our production house, 'Lorin Studios' based in Singapore. We produce microfilms as well as podcasts, talkshows and events. Our logo is a stylized icon of our director, who is also the executive producer and host of our programs, Lorin. Our main company colors are Red, Black and white. We would like a clean, minimalist design incorporating our existing company logo that conveys a sense of urbanism and elegance.

Logo and font files are attached. f

Target Market(s)

We focus on lifestyle media rather than entertainment.

Industry/Entity Type

Boutique

Font styles to use
Serif
Sans Serif

Colors
ec1f27
ffffff
000000

Requirements
Must have
• Our company logo and at least one of our company colors.
Nice to have
• Our address and contact information.
Should not have
• Changes made to the company logo (using only certain parts of it is fine though)

```html
<!DOCTYPE html>
<html lang="en">
<head>
<meta charset="utf-8">
<title>Lorin Studios — Stationery</title>
<link rel="stylesheet" href="https://fonts.googleapis.com/css2?family=EB+Garamond:wght@400;600;700&display=swap">
<style>
  :root{
    --red:#ec1f27;
    --black:#000000;
    --ink:#111111;
    --white:#ffffff;
    --paper:#fbfbfb;
    --grey-ring:#3a3a3a;
    --backdrop:#8a8484;
    --serif:"EB Garamond", Georgia, serif;
  }
  *{box-sizing:border-box;margin:0;padding:0}
  html,body{width:1200px;height:1080px;overflow:hidden}
  body{background:var(--backdrop);font-family:var(--serif);color:var(--ink);position:relative}

  .piece{position:absolute;overflow:hidden}
  .disc{position:absolute;border-radius:50%}

  /* wordmark */
  .wordmark{display:flex;align-items:center;gap:6px}
  .wordmark__dot{width:9px;height:9px;border-radius:50%;background:var(--red);flex:none}
  .wordmark__name{font-family:var(--serif);font-weight:700;line-height:1;text-transform:uppercase;letter-spacing:.04em}

  /* letterhead */
  .letterhead{left:40px;top:40px;width:440px;height:622px;background:var(--paper);
    border-top:3px solid var(--black);border-bottom:3px solid var(--red)}
  .letterhead .corner-red{width:420px;height:420px;left:225px;top:-215px;background:var(--red)}
  .letterhead .corner-ring{width:230px;height:230px;left:-120px;top:495px;border:38px solid var(--black)}
  .letterhead .wordmark{position:absolute;left:66px;top:44px}
  .letterhead .wordmark__name{font-size:13px;color:var(--black)}
  .letterhead .contact{position:absolute;left:282px;top:40px;color:var(--white);font-size:6.6px;line-height:1.65}
  .letterhead .salutation{position:absolute;left:68px;top:165px;font-weight:700;font-size:12px}
  .letterhead .body{position:absolute;left:68px;right:62px;top:224px;font-size:7.5px;line-height:1.38;font-weight:600}
  .letterhead .body p{text-align:justify;text-indent:12px;margin-bottom:14px}
  .letterhead .signoff{position:absolute;right:68px;top:432px;text-align:right;font-size:7.6px;font-weight:700;line-height:1.35}
  .letterhead .signature{position:absolute;right:66px;top:472px;width:112px;height:30px;
    background:linear-gradient(90deg,rgba(0,0,0,.08),rgba(0,0,0,.16));border-radius:3px}

  /* folder */
  .folder{left:520px;top:40px;width:400px;height:560px;background:#1b1b1b;border-radius:0 6px 10px 0}
  .folder .ring-outer{width:240px;height:240px;left:280px;top:160px;background:var(--black)}
  .folder .ring-grey{width:206px;height:206px;left:297px;top:177px;background:var(--grey-ring)}
  .folder .ring-white{width:176px;height:176px;left:312px;top:192px;background:var(--white)}
  .folder .ring-gap{width:166px;height:166px;left:317px;top:197px;background:var(--black)}
  .folder .ring-red{width:150px;height:150px;left:325px;top:205px;background:var(--red)}

  /* business cards */
  .card{width:200px;height:120px}
  .card--front{left:960px;top:40px;background:var(--paper)}
  .card--front .corner-red{width:44px;height:44px;left:178px;top:-22px;background:var(--red)}
  .card--front .corner-black{width:44px;height:44px;left:-22px;top:98px;background:var(--black)}
  .card--front .wordmark{position:absolute;left:0;right:0;top:52px;justify-content:center}
  .card--front .wordmark__name{font-size:11px;color:var(--black)}

  .card--back{left:960px;top:190px;background:var(--red);color:var(--white)}
  .card--back .corner-black{width:44px;height:44px;left:-22px;top:-22px;background:var(--black)}
  .card--back .corner-white{width:44px;height:44px;left:178px;top:98px;background:var(--white)}
  .card--back .wordmark{position:absolute;left:0;right:0;top:14px;justify-content:center}
  .card--back .wordmark__dot{width:6px;height:6px;background:var(--white)}
  .card--back .wordmark__name{font-size:8px;color:var(--white)}
  .card--back .person{position:absolute;left:0;right:0;top:36px;text-align:center}
  .card--back .person__name{font-size:8px;font-weight:600}
  .card--back .person__role{font-size:5.5px;font-style:italic}
  .card--back .details{position:absolute;left:14px;right:24px;top:78px;display:flex;gap:10px;font-size:5px;line-height:1.9}
  .card--back .details__col{flex:1}
  .card--back .details__rule{width:1px;height:20px;background:var(--white);margin-top:2px}

  /* envelope */
  .envelope{left:40px;top:700px;width:400px;height:290px;background:var(--red);border-bottom:3px solid #333}
  .envelope .wordmark{position:absolute;left:0;right:0;top:96px;justify-content:center}
  .envelope .wordmark__dot{width:12px;height:12px;background:var(--white)}
  .envelope .wordmark__name{font-size:22px;color:var(--white)}
</style>
</head>
<body>

  <section class="piece letterhead" aria-label="Letterhead">
    <div class="disc corner-red"></div>
    <div class="disc corner-ring"></div>
    <div class="wordmark"><span class="wordmark__dot"></span><span class="wordmark__name">Lorin Studios</span></div>
    <address class="contact" style="font-style:normal">
      48 Kelvin Road, &nbsp;/ City Name, Country Name<br>
      t. 65 (00) 418 702XX<br>
      e. hello@lorinstudios.sg
    </address>
    <h1 class="salutation">Lorem Ipsum,</h1>
    <div class="body">
      <p>Lorem ipsum dolor sit amet, consectetur adipisicing elit, sed do eiusmod tempor incididunt ut labore et dolore magna aliqua. Ut enim ad minim veniam, quis nostrud exercitation ullamco laboris nisi ut aliquip ex ea commodo consequat. Duis aute irure dolor in reprehenderit in voluptate velit esse cillum dolore eu fugiat nulla pariatur. Excepteur sint occaecat cupidatat non proident, sunt in culpa qui officia deserunt mollit anim id est laborum. Sed ut perspiciatis unde omnis iste natus error sit voluptatem accusantium doloremque laudantium, totam rem aperi-</p>
      <p>Lorem ipsum dolor sit amet, consectetur adipisicing elit, sed do eiusmod tempor incididunt ut labore et dolore magna aliqua. Ut enim ad minim veniam, quis nostrud exercitation ullamco laboris nisi ut aliquip ex ea commodo consequat. Duis aute irure dolor in reprehenderit in voluptate velit esse cillum dolore eu fugiat nulla pariatur. Excepteur sint occaecat cupidatat non proident, sunt in culpa qui officia deserunt mollit anim id est laborum. Sed ut perspiciatis unde omnis iste natus error sit voluptatem accusantium doloremque laudantium, totam rem aperi-</p>
    </div>
    <div class="signoff">Your Sincerely,<br>Wen Hara</div>
    <div class="signature" role="img" aria-label="Handwritten signature of Wen Hara"></div>
  </section>

  <section class="piece folder" aria-label="Presentation folder">
    <div class="disc ring-outer"></div>
    <div class="disc ring-grey"></div>
    <div class="disc ring-white"></div>
    <div class="disc ring-gap"></div>
    <div class="disc ring-red"></div>
  </section>

  <section class="piece card card--front" aria-label="Business card front">
    <div class="disc corner-red"></div>
    <div class="disc corner-black"></div>
    <div class="wordmark"><span class="wordmark__dot"></span><span class="wordmark__name">Lorin Studios</span></div>
  </section>

  <section class="piece card card--back" aria-label="Business card back">
    <div class="disc corner-black"></div>
    <div class="disc corner-white"></div>
    <div class="wordmark"><span class="wordmark__dot"></span><span class="wordmark__name">Lorin Studios</span></div>
    <div class="person">
      <div class="person__name">Mei Okada</div>
      <div class="person__role">Director</div>
    </div>
    <div class="details">
      <div class="details__col">t. 65 (00) 418 702XX<br>e. hello@lorinstudios.sg</div>
      <div class="details__rule"></div>
      <div class="details__col">48 Kelvin Road<br>City Name, Country Name</div>
    </div>
  </section>

  <section class="piece envelope" aria-label="Envelope">
    <div class="wordmark"><span class="wordmark__dot"></span><span class="wordmark__name">Lorin Studios</span></div>
  </section>

</body>
</html>
```